Tervolan Pty Ltd professional business card

A professional business card template using the colours from the supplied logo.
Clean crisp lines while, Modern while not being over the top.

Target Market(s)

Construction, commerical and industrial

Industry/Entity Type

Communications

Contact Information for Business Card

For a Communications, IT, Optical fibre installation company

Colors
37b8a4

```html
<!DOCTYPE html>
<html lang="en">
<head>
<meta charset="utf-8">
<title>Tervolan Pty Ltd – Business Card</title>
<link href="https://fonts.googleapis.com/css2?family=Lato:wght@400;700;900&display=swap" rel="stylesheet">
<style>
  :root {
    --backdrop: #2b2b2d;
    --card: #252527;
    --teal: #1d9aa6;
    --logo-grey: #6e6f73;
    --text-light: #f2f2f2;
    --shadow: rgba(0, 0, 0, 0.55);
  }
  * { box-sizing: border-box; margin: 0; padding: 0; }
  html, body {
    width: 1200px;
    height: 970px;
    overflow: hidden;
    background: var(--backdrop);
    font-family: "Lato", sans-serif;
  }
  .stage {
    position: relative;
    width: 1200px;
    height: 970px;
  }
  .card {
    position: absolute;
    left: 220px;
    width: 760px;
    height: 420px;
    background: var(--card);
    box-shadow: 0 14px 30px var(--shadow);
    overflow: hidden;
  }
  .card::after {
    content: "";
    position: absolute;
    left: 0; right: 0; bottom: 0;
    height: 9px;
    background: var(--teal);
  }
  .card--front { top: 48px; }
  .card--back { top: 502px; }

  .brand {
    display: flex;
    align-items: center;
    gap: 14px;
  }
  .brand__mark {
    width: 22px;
    height: 22px;
    border-radius: 50%;
    background: var(--teal);
  }
  .brand__name {
    font-weight: 700;
    color: var(--logo-grey);
    letter-spacing: 2px;
    line-height: 1;
  }

  .card--front .brand {
    position: absolute;
    left: 62px;
    top: 62px;
  }
  .card--front .brand__name { font-size: 72px; }

  .person {
    position: absolute;
    left: 70px;
    top: 178px;
  }
  .person__name {
    font-size: 38px;
    font-weight: 900;
    color: var(--teal);
    letter-spacing: 0.5px;
    line-height: 1.05;
  }
  .person__role {
    font-size: 22px;
    color: var(--text-light);
    margin-top: 4px;
  }

  .contact {
    position: absolute;
    left: 70px;
    top: 282px;
    list-style: none;
  }
  .contact__item {
    display: flex;
    align-items: center;
    gap: 18px;
    font-size: 21px;
    color: var(--text-light);
    height: 32px;
  }
  .contact__icon {
    width: 20px;
    height: 20px;
    flex: none;
  }

  .address {
    position: absolute;
    right: 46px;
    bottom: 40px;
    text-align: right;
    font-size: 20px;
    line-height: 1.35;
    color: var(--text-light);
  }

  .card--back .brand {
    position: absolute;
    right: 56px;
    top: 150px;
  }
  .card--back .brand__mark { width: 26px; height: 26px; }
  .card--back .brand__name { font-size: 84px; }
</style>
</head>
<body>
<main class="stage">

  <section class="card card--front" aria-label="Business card front">
    <div class="brand">
      <span class="brand__mark"></span>
      <span class="brand__name">TERVOLAN</span>
    </div>

    <div class="person">
      <p class="person__name">MARA ELLISON</p>
      <p class="person__role">Founder &amp; CEO</p>
    </div>

    <ul class="contact">
      <li class="contact__item">
        <svg class="contact__icon" viewBox="0 0 24 24" aria-hidden="true">
          <path fill="#1d9aa6" d="M6.6 10.8a15.1 15.1 0 0 0 6.6 6.6l2.2-2.2c.3-.3.7-.4 1-.2 1.1.4 2.3.6 3.6.6.6 0 1 .4 1 1V20c0 .6-.4 1-1 1A17 17 0 0 1 3 4c0-.6.4-1 1-1h3.5c.6 0 1 .4 1 1 0 1.3.2 2.5.6 3.6.1.3 0 .7-.2 1z"/>
        </svg>
        <span>1234567890</span>
      </li>
      <li class="contact__item">
        <svg class="contact__icon" viewBox="0 0 24 24" aria-hidden="true">
          <rect x="2" y="5" width="20" height="14" rx="1" fill="#1d9aa6"/>
          <path d="M2.5 5.5 12 13l9.5-7.5" fill="none" stroke="#252527" stroke-width="1.6"/>
        </svg>
        <span>info@yourmail.com</span>
      </li>
      <li class="contact__item">
        <svg class="contact__icon" viewBox="0 0 24 24" aria-hidden="true">
          <g fill="none" stroke="#1d9aa6" stroke-width="1.8">
            <circle cx="12" cy="12" r="9.5"/>
            <ellipse cx="12" cy="12" rx="4" ry="9.5"/>
            <path d="M2.5 12h19M4 7h16M4 17h16"/>
          </g>
        </svg>
        <span>www.yourwebsite.com</span>
      </li>
    </ul>

    <address class="address">
      1234 First Line Address<br>
      5678 Second Line Address
    </address>
  </section>

  <section class="card card--back" aria-label="Business card back">
    <div class="brand">
      <span class="brand__mark"></span>
      <span class="brand__name">TERVOLAN</span>
    </div>
  </section>

</main>
</body>
</html>
```